Business Card Design

Online clothing womens clothing store, I sell my clothing online and at the markets.

i would like the attached picture on the front of the card and the contact information on the back.

Industry/Entity Type

Business

Contact Information for Business Card

Velvet Harbour
Marnie Talbot
(Instagram symbol) _velvet_harbour_
(Facebook symbol) www.facepage-example.com/velvetharbourau/

W : www.velvetharbour-example.com.au
E : info@velvetharbour-example.com.au
P : 0491876324

```html
<!DOCTYPE html>
<html lang="en">
<head>
<meta charset="utf-8">
<title>Velvet Harbour – Business Card</title>
<link href="https://fonts.googleapis.com/css2?family=Special+Elite&family=Arimo:wght@400&display=swap" rel="stylesheet">
<style>
  :root {
    --page-bg: #e9e6e1;
    --card-black: #0d0d0d;
    --card-charcoal: #2a2a2a;
    --paper-light: #f2f2f2;
    --paper-mid: #c9c9c9;
    --smoke-dark: #2e2e2e;
    --photo-green: #7b8868;
    --photo-sand: #cbc1ab;
    --photo-shade: #5c6450;
    --ink-white: #ffffff;
    --ink-logo: #2b2b2b;
    --rule-grey: #cfcfcf;
  }
  * { box-sizing: border-box; margin: 0; padding: 0; }
  html, body { width: 1200px; height: 902px; overflow: hidden; }
  body {
    background: var(--page-bg);
    display: flex;
    flex-direction: column;
    align-items: center;
    justify-content: center;
    gap: 40px;
  }
  .card {
    position: relative;
    width: 680px;
    height: 389px;
    overflow: hidden;
    box-shadow: 0 6px 18px rgba(0,0,0,.18);
  }

  /* Front */
  .card-front {
    background: linear-gradient(100deg, var(--paper-mid) 0%, var(--paper-light) 35%, #e4e4e4 60%, #bdbdbd 100%);
  }
  .front-portrait {
    position: absolute;
    right: -40px;
    top: -60px;
    width: 480px;
    height: 400px;
    background: radial-gradient(ellipse at 55% 45%, var(--smoke-dark) 0%, #4a4a4a 35%, rgba(120,120,120,.6) 60%, rgba(220,220,220,0) 75%);
  }
  .front-wordmark {
    position: absolute;
    right: 34px;
    bottom: 70px;
    font-family: "Special Elite", monospace;
    font-size: 60px;
    letter-spacing: 3px;
    color: var(--ink-white);
    line-height: 1;
  }

  /* Back */
  .card-back { background: linear-gradient(160deg, var(--card-charcoal) 0%, var(--card-black) 45%); }
  .back-shapes { position: absolute; inset: 0; }
  .back-wordmark {
    position: absolute;
    left: 150px;
    top: 118px;
    font-family: "Special Elite", monospace;
    font-size: 46px;
    letter-spacing: 7px;
    color: var(--ink-logo);
    line-height: 1;
  }
  .holder-name {
    position: absolute;
    left: 70px;
    top: 300px;
    font-family: "Special Elite", monospace;
    font-size: 25px;
    letter-spacing: 5px;
    color: var(--ink-white);
    text-transform: uppercase;
  }
  .contact-divider {
    position: absolute;
    left: 392px;
    top: 228px;
    width: 1px;
    height: 136px;
    background: var(--rule-grey);
  }
  .contact-list {
    position: absolute;
    left: 408px;
    top: 232px;
    list-style: none;
    font-family: "Arimo", Arial, sans-serif;
    font-size: 15px;
    color: var(--ink-white);
  }
  .contact-list li {
    display: flex;
    align-items: center;
    gap: 10px;
    height: 26px;
  }
  .contact-icon {
    width: 15px;
    height: 15px;
    flex: none;
    background: var(--ink-white);
    border-radius: 2px;
  }
  .contact-icon svg { display: block; width: 15px; height: 15px; }
</style>
</head>
<body>

  <section class="card card-front" aria-label="Card front">
    <div class="front-portrait" role="img" aria-label="Black and white double-exposure portrait photograph of a woman fading into mist"></div>
    <div class="front-wordmark">VELVET HARBOUR</div>
  </section>

  <section class="card card-back" aria-label="Card back">
    <svg class="back-shapes" viewBox="0 0 680 389" width="680" height="389">
      <defs>
        <linearGradient id="photoTone" x1="0" y1="1" x2="1" y2="0">
          <stop offset="0" stop-color="var(--photo-shade)"/>
          <stop offset="0.45" stop-color="var(--photo-sand)"/>
          <stop offset="1" stop-color="var(--photo-green)"/>
        </linearGradient>
      </defs>
      <polygon role="img" aria-label="Photograph of a woman in a long dress standing on railway tracks beside trees and a painted mural"
        points="0,0 680,0 680,150 608,208 120,208 88,236 0,236" fill="url(#photoTone)"/>
      <polyline points="0,246 92,246 124,218 612,218 680,162" fill="none" stroke="var(--rule-grey)" stroke-width="5"/>
    </svg>

    <div class="back-wordmark">VELVET HARBOUR</div>
    <div class="holder-name">Marnie Talbot</div>
    <div class="contact-divider"></div>

    <ul class="contact-list">
      <li>
        <span class="contact-icon">
          <svg viewBox="0 0 15 15"><path d="M4 3 L6 3 L7 5.5 L5.8 6.6 Q7 8.6 8.6 9.4 L9.6 8.2 L12 9.2 L12 11.2 Q11 12.3 9.5 12 Q4.2 10.5 3 5 Q2.8 3.7 4 3 Z" fill="var(--card-black)"/></svg>
        </span>0491876324
      </li>
      <li><span class="contact-icon"></span>velvetharbourau</li>
      <li><span class="contact-icon"></span>velvet_harbour</li>
      <li>
        <span class="contact-icon">
          <svg viewBox="0 0 15 15"><circle cx="7.5" cy="7.5" r="4.6" fill="none" stroke="var(--card-black)" stroke-width="1.2"/><path d="M2.9 7.5 H12.1 M7.5 2.9 Q4.8 7.5 7.5 12.1 M7.5 2.9 Q10.2 7.5 7.5 12.1" fill="none" stroke="var(--card-black)" stroke-width="1"/></svg>
        </span>www.velvetharbour-example.com.au
      </li>
      <li>
        <span class="contact-icon">
          <svg viewBox="0 0 15 15"><rect x="2.5" y="4" width="10" height="7" fill="none" stroke="var(--card-black)" stroke-width="1.2"/><path d="M2.5 4 L7.5 8 L12.5 4" fill="none" stroke="var(--card-black)" stroke-width="1.2"/></svg>
        </span>info@velvetharbour-example.com.au
      </li>
    </ul>
  </section>

</body>
</html>
```